Manufacturing Company WordPress Website Design

Looking for a modern WordPress design for a manufacturer of oil separation and coolant recycling products called BrightFloe. This is a business-to-business marketer in the industrial manufacturing sector. BrightFloe sells to CNC manufacturing companies and their products are known as some of the best tools in the world for skimming and separating floating oils, metallic fines, and other contaminants from industrial process fluids.

The winning design will be based on a responsive WP theme. Include the theme name if your design is selected by the client. Provide Home, Product and Case Study page views with your submission.

THE BRIGHTFLOE BRAND
The BrightFloe brand is all about connection and partnership. They are down-to-earth, relatable, helpful and fun to hang out with. The brand voice is humble, authentic and helpful and they are driven by connection, togetherness and inclusion.

The BrightFloe target audience is plant managers, enterprise engineers and business owners in CNC machining manufacturing companies across a variety of industries (automotive, aerospace, energy, medical and transportation).

BrightFloe is looking for a clean, modern website that better represents their brand with a more polished and professional design. It should be:
- responsive and mobile-friendly
- easily findable for key search criteria
- a source for improved lead generation for prospective sales
- more easily editable

A design that is oriented toward these goals will be selected as the winner.

The winning designer may be chosen to code the website, or to code the initial pages in the concept design.

Current Website:
https://brightfloe-example.com/index.html

Competitors:
https://www.kelvora-example.com/
https://www.tundix-example.com/
https://www.voltarin-example.com/

Sites We Like:
https://northgateweldworks-example.com/
- we like the clean layout of the home page in a grid-like design, simple header and footer, the parallax scrolling, and the mobile responsiveness.

https://www.kelvora-example.com/fluid-filtration/sentinel-coolant-recycling-systems/
- we like the way the content is presented on the Kelvora product page - specifically, we like the use of the tabs below the main product images to present a lot of content without it looking overwhelmingly busy.

https://pinecrestpanes-example.com/healthcare/harborview-care-clinic/
- we like the way Pinecrest Panes presents their cases studies with a combination of useful information highlighted by informative icons and pictures to present key statistics in the case study. We would like the BrightFloe case studies to almost feel like an infographic presentation on the website.

Attached files to help your designs:
- Brand Identity Guidelines
- BrightFloe Logos
- Product Photos
- Brand Photos
- Home page content
- Coolant Recycling product page content
- Case Study page content
- Site Map
- Wire Frames

Target Market(s)

Industry/Entity Type

Industrial

Coding

Coded - Design and coding required

Number of Pages Required

3 page

Font styles to use
Sans Serif
Other font styles liked:
• DINPro is used on all collateral - see brand guidelines

Requirements
Must have
• See the brand guidelines file attached for colors and logo usage

```html
<!DOCTYPE html>
<html lang="en">
<head>
<meta charset="utf-8">
<title>BrightFloe — Oil Separation and Coolant Recycling</title>
<link rel="stylesheet" href="https://fonts.googleapis.com/css2?family=Roboto:wght@400;500;700&family=Lato:wght@400;700;900&display=swap">
<style>
:root{
  --brand-blue:#0b3f8f;
  --action-blue:#1a73d9;
  --ink:#2b2b2b;
  --muted:#5a5a5a;
  --page:#f8f8f8;
  --card:#efefef;
  --card-curve:#f7f7f7;
  --alert-red:#d4211c;
  --navy:#04163a;
  --bar:#232323;
  --white:#ffffff;
}
*{box-sizing:border-box;margin:0;padding:0}
html,body{width:1200px;height:4298px;overflow:hidden}
body{position:relative;background:var(--page);font-family:'Lato',sans-serif;color:var(--ink)}
.abs{position:absolute}

/* Header and hero */
.hero{left:0;top:0;width:1200px;height:474px;background:linear-gradient(180deg,#5d5a55 0%,#4a4744 45%,#3b342c 100%)}
.site-brand{left:127px;top:22px;display:flex;align-items:center;gap:10px;color:var(--white);font-weight:700;font-size:17px;letter-spacing:.5px}
.site-brand .mark{width:34px;height:34px;border-radius:50%;border:2px solid var(--white)}
.main-nav{right:262px;top:31px;display:flex;gap:24px}
.main-nav a{color:var(--white);text-decoration:none;font-size:12px}
.hero-arrow{top:225px;width:14px;height:24px}
.hero-title{left:0;width:1200px;top:168px;text-align:center;color:var(--white);font-weight:700;font-size:54px;letter-spacing:-.5px}
.hero-cta{left:434px;top:252px;width:330px;height:48px;border:2px solid var(--alert-red);color:var(--white);font-family:'Roboto',sans-serif;font-weight:700;font-size:14px;letter-spacing:2px;display:flex;align-items:center;justify-content:center}

/* About */
.about-title{left:158px;top:544px;width:560px;font-family:'Roboto',sans-serif;font-weight:700;font-size:28px;line-height:33px;color:var(--brand-blue)}
.about-text{left:158px;top:626px;width:582px;font-size:12.6px;line-height:24.6px;color:var(--muted)}
.about-photo{left:758px;top:544px;width:284px;height:214px;background:linear-gradient(135deg,#8a8f95,#4d5560 55%,#c26a2d)}

/* Products */
.section-title{left:0;width:1200px;text-align:center;font-family:'Roboto',sans-serif}
.products-title{top:856px;font-weight:700;font-size:40px;color:var(--brand-blue)}
.product-card{width:291px;background:var(--card-curve);overflow:hidden}
.product-card::before{content:"";position:absolute;left:-170px;top:-40px;width:470px;height:560px;border-radius:50%;background:var(--card)}
.product-photo{position:absolute;z-index:1}
.product-name{position:absolute;left:16px;width:260px;z-index:1;font-family:'Roboto',sans-serif;font-weight:700;font-size:23px;line-height:28px;color:var(--brand-blue)}
.product-text{position:absolute;left:16px;width:262px;z-index:1;font-size:12px;line-height:23.4px;color:var(--muted)}
.product-actions{position:absolute;left:38px;z-index:1;display:flex;align-items:center;gap:55px}
.btn{display:inline-flex;align-items:center;justify-content:center;background:var(--action-blue);color:var(--white);font-size:12px;text-decoration:none}
.btn-learn{width:112px;height:41px}
.video-link{width:38px;height:38px;border-radius:5px;background:var(--alert-red)}

/* Engineering support */
.support-band{left:0;top:1891px;width:1200px;height:900px;background:var(--white)}
.support-title{top:2008px;font-weight:400;font-size:29px;color:#1d2533}
.support-lead{left:300px;top:2060px;width:600px;text-align:center;font-size:12px;line-height:23.4px;color:var(--muted)}
.founder-shape{left:195px;top:2180px;width:361px;height:349px;border-radius:48% 52% 46% 54%/50% 44% 56% 50%;background:#f1f1f1}
.founder-photo{left:282px;top:2158px;width:204px;height:371px;border-radius:0 0 102px 102px;background:linear-gradient(180deg,#d9d9d9 0%,#6f747c 40%,#2f3440 100%)}
.founder-caption{left:195px;top:2549px;width:361px;text-align:center;font-size:12px;color:#444}
.accordion{left:628px;top:2196px;width:422px;height:341px;background:var(--white);box-shadow:0 4px 20px rgba(0,0,0,.07)}
.acc-item{border-bottom:1px solid #ececec;padding:0 22px;display:flex;align-items:center;gap:22px;font-size:12.2px;font-weight:700;color:#333}
.acc-item.open{color:var(--action-blue)}
.acc-body{padding:18px 24px;font-size:12px;line-height:23.4px;color:var(--muted);border-bottom:1px solid #ececec}

/* Partners */
.partners-label{left:178px;top:2712px;font-family:'Roboto',sans-serif;font-weight:700;font-size:15px;color:#333}
.partners-divider{left:329px;top:2682px;width:1px;height:80px;background:#cfcfcf}
.partner-badge{height:30px;background:#3a7bd5;opacity:.75;border-radius:4px}

/* Testimonials */
.testimonials-bg{left:0;top:2790px;width:1200px;height:832px;background:#f2f2f2}
.testimonials-title{top:2940px;font-weight:400;font-size:29px;color:#1d2533}
.quote-card{background:var(--white);padding:24px 24px 0;box-shadow:0 2px 14px rgba(0,0,0,.04)}
.quote-text{font-size:12px;line-height:23.4px;color:var(--muted)}
.quote-author{display:flex;align-items:center;gap:14px;margin-top:12px}
.avatar{width:44px;height:44px;border-radius:50%;background:linear-gradient(135deg,#d8c2ad,#8a7565)}
.author-name{font-size:12.5px;font-weight:700;color:#222}
.author-place{font-size:10.5px;color:#777}
.btn-cases{left:526px;top:3498px;width:148px;height:36px}

/* Footer */
.footer{left:0;top:3622px;width:1200px;height:287px;background:var(--navy);padding:7px 0 0 55px}
.footer-heading{font-family:'Roboto',sans-serif;font-weight:700;font-size:14px;color:#24355a;height:28px}
.footer-links{list-style:none}
.footer-links li{height:28.4px;font-size:12px;color:var(--white)}
.bottom-bar{left:0;top:4225px;width:1200px;height:73px;background:var(--bar);color:var(--white);font-size:12px;padding:29px 0 0 158px}
</style>
</head>
<body>

<header class="abs hero" role="img" aria-label="Close-up of a CNC milling tool cutting metal with chips scattered across the machine bed"></header>
<div class="abs site-brand"><span class="mark"></span>BrightFloe</div>
<nav class="abs main-nav"><a href="#">Home</a><a href="#">Products</a><a href="#">Case Studies</a><a href="#">About</a><a href="#">Contact</a></nav>
<svg class="abs hero-arrow" style="left:12px" viewBox="0 0 14 24"><path d="M11 3 3 12l8 9" fill="none" stroke="#fff" stroke-width="2.5"/></svg>
<svg class="abs hero-arrow" style="right:12px" viewBox="0 0 14 24"><path d="M3 3l8 9-8 9" fill="none" stroke="#fff" stroke-width="2.5"/></svg>
<h1 class="abs hero-title">Extended Tool Life</h1>
<a class="abs hero-cta">START YOUR PROJECT NOW !</a>

<h2 class="abs about-title">The Global Leader in Oil Separation and Coolant Recycling</h2>
<p class="abs about-text">BrightFloe products are known as some of the best tools in the world for skimming and separating floating oils, metallic fines, and other contaminants from industrial process fluids. Our success has been built on a simple foundation: we manufacture the best products in the industry with superior customer service. For you, that means easy-to-use, rugged and durable systems that you can depend on well into the future. To learn more about how some of the largest companies in the world are using our BrightFloe products to drastically reduce costs and operate more efficiently.</p>
<div class="abs about-photo" role="img" aria-label="Plant engineer in hard hat and safety vest reviewing a tablet on the factory floor"></div>

<h2 class="abs section-title products-title">Our Most Popular Products</h2>

<article class="abs product-card" style="left:150px;top:930px;height:449px">
  <div class="product-photo" role="img" aria-label="Blue oil water separator unit" style="left:70px;top:28px;width:135px;height:130px;background:linear-gradient(135deg,#b7bcc2,#2a4fa8)"></div>
  <h3 class="product-name" style="top:180px">Oil Water Separators</h3>
  <p class="product-text" style="top:225px">Best tools in the world for skimming and separating floating oils and other contaminants from industrial process fluids.</p>
  <div class="product-actions" style="top:338px"><a class="btn btn-learn">Learn More</a><span class="video-link"></span></div>
</article>
<article class="abs product-card" style="left:450px;top:930px;height:449px">
  <div class="product-photo" role="img" aria-label="Blue coolant recycling system on wheels" style="left:65px;top:22px;width:145px;height:135px;background:linear-gradient(135deg,#9aa3ad,#1c3fa0)"></div>
  <h3 class="product-name" style="top:174px">Coolant Recycling Systems</h3>
  <p class="product-text" style="top:248px">Highly reliable fluid treatment systems designed for easy installation and maintenance to separate contaminated floating oils and solids from your valuable machining coolants.</p>
  <div class="product-actions" style="top:385px"><a class="btn btn-learn">Learn More</a><span class="video-link"></span></div>
</article>
<article class="abs product-card" style="left:750px;top:930px;height:449px">
  <div class="product-photo" role="img" aria-label="Magnetic separator column" style="left:100px;top:22px;width:80px;height:135px;background:linear-gradient(180deg,#c9ccd1,#3f5fb0)"></div>
  <h3 class="product-name" style="top:180px">Magnetic Separators</h3>
  <p class="product-text" style="top:225px">Magnetic separators eliminate the use of filter consumables, are easy to implement, simple to operate, and require minimal maintenance.</p>
  <div class="product-actions" style="top:338px"><a class="btn btn-learn">Learn More</a><span class="video-link"></span></div>
</article>

<article class="abs product-card" style="left:150px;top:1397px;height:478px">
  <div class="product-photo" role="img" aria-label="Floating suction skimmer with twin floats" style="left:85px;top:18px;width:100px;height:140px;background:linear-gradient(180deg,#d0d0d0,#3a3a3a)"></div>
  <h3 class="product-name" style="top:179px">Floating Suction Skimmers</h3>
  <p class="product-text" style="top:253px">The multi-patented Suction Skimmer is the most efficient and most durable device available for skimming and removing floating oil and contaminants from industrial process fluids.</p>
  <div class="product-actions" style="top:413px"><a class="btn btn-learn">Learn More</a><span class="video-link"></span></div>
</article>
<article class="abs product-card" style="left:450px;top:1397px;height:478px">
  <div class="product-photo" role="img" aria-label="Blue sump cleaner tank on wheels" style="left:38px;top:18px;width:215px;height:168px;background:linear-gradient(135deg,#8d98a8,#1b3ea6)"></div>
  <h3 class="product-name" style="top:206px">Sump Cleaner</h3>
  <p class="product-text" style="top:251px">Sump cleaners serve as a great complementary product to the FluidCircuit Coolant Recycling Systems. The Sump cleaner greatly reduces the amount of labor required to effectively clean your sumps.</p>
  <div class="product-actions" style="top:411px"><a class="btn btn-learn">Learn More</a><span class="video-link"></span></div>
</article>
<article class="abs product-card" style="left:750px;top:1397px;height:478px">
  <div class="product-photo" role="img" aria-label="Stainless steel skimming center installed beside a parts washer" style="left:68px;top:15px;width:163px;height:128px;background:linear-gradient(135deg,#b9bcbf,#6c7278 60%,#4a6fa0)"></div>
  <h3 class="product-name" style="top:161px">Skimming Centers</h3>
  <p class="product-text" style="top:206px">For parts washing and coolant applications, it is more effective to skim and separate floating oils outside the washer or coolant tank where the fluids are continuously turbulent.</p>
  <div class="product-actions" style="top:340px"><a class="btn btn-learn">Learn More</a><span class="video-link"></span></div>
</article>

<div class="abs support-band"></div>
<h2 class="abs section-title support-title">Run Cleaner with Our Engineering Support</h2>
<p class="abs support-lead">Our application engineers help plant teams pick, install and tune the right separator for every machine. Cleaner coolant, longer tool life.</p>
<div class="abs founder-shape"></div>
<div class="abs founder-photo" role="img" aria-label="Portrait of the company founder in a grey suit"></div>
<p class="abs founder-caption">Dr. Alan Mercer — Founder &amp; CEO.</p>

<div class="abs accordion">
  <div class="acc-item open" style="height:76px"><svg width="8" height="6" viewBox="0 0 8 6"><path d="M0 0h8L4 6z" fill="#1a73d9"/></svg>Cut Coolant Costs</div>
  <div class="acc-body">Removing tramp oil and fines keeps coolant in service for months, not weeks. Most plants see lower purchase and disposal costs within the first year.</div>
  <div class="acc-item" style="height:76px"><svg width="6" height="8" viewBox="0 0 6 8"><path d="M0 0l6 4-6 4z" fill="#333"/></svg>Find The Right Separator For Your Machines</div>
  <div class="acc-item" style="height:76px;border-bottom:0"><svg width="6" height="8" viewBox="0 0 6 8"><path d="M0 0l6 4-6 4z" fill="#333"/></svg>Learn From Our Application Engineers</div>
</div>

<p class="abs partners-label">Industry Partners</p>
<div class="abs partners-divider"></div>
<div class="abs partner-badge" style="left:384px;top:2707px;width:84px"></div>
<div class="abs partner-badge" style="left:556px;top:2705px;width:90px;height:34px"></div>
<div class="abs partner-badge" style="left:734px;top:2707px;width:86px"></div>
<div class="abs partner-badge" style="left:913px;top:2703px;width:80px;height:36px;border-radius:18px"></div>

<div class="abs testimonials-bg"></div>
<svg class="abs" style="left:0;top:2780px" width="1200" height="60" viewBox="0 0 1200 60" preserveAspectRatio="none"><path d="M0 60V45C200 10 380 10 600 30S1000 5 1200 20V60Z" fill="#f2f2f2"/><path d="M0 0h1200v20C1000 5 820 50 600 30S200 10 0 45Z" fill="#fff"/></svg>
<h2 class="abs section-title testimonials-title">What Our Customers Have to Say</h2>

<div class="abs quote-card" style="left:174px;top:3033px;width:410px;height:148px">
  <p class="quote-text">BrightFloe's ability to filter coolant has surpassed our expectations.</p>
  <div class="quote-author"><span class="avatar"></span><div><p class="author-name">Marcus Hale</p><p class="author-place">From Dallas, USA</p></div></div>
</div>
<div class="abs quote-card" style="left:616px;top:3033px;width:410px;height:148px">
  <p class="quote-text">It's not often you buy a piece of machinery and hit a grand slam. With BrightFloe we did</p>
  <div class="quote-author"><span class="avatar"></span><div><p class="author-name">Nadia Voss</p><p class="author-place">From Australia</p></div></div>
</div>
<div class="abs quote-card" style="left:174px;top:3213px;width:410px;height:244px">
  <p class="quote-text">We installed our first BrightFloe unit in January 2009 and had outstanding results. When we opened up a new plant last year, we installed a BrightFloe there as well. This is a great product and is easily customizable to fit anyone's needs.</p>
  <div class="quote-author"><span class="avatar"></span><div><p class="author-name">Owen Pratt</p><p class="author-place">From Japan</p></div></div>
</div>
<div class="abs quote-card" style="left:616px;top:3213px;width:410px;height:244px">
  <p class="quote-text">We have reduced our coolant usage from 3 barrels a month to about one, and reduced our waste coolant by 95%. Based on that alone the unit paid for itself in about 9 months, and now we are realizing a savings of about $2400 a month. The BrightFloe performs exactly as advertised, very satisfied, would not be without one.</p>
  <div class="quote-author"><span class="avatar"></span><div><p class="author-name">Liam Carver</p><p class="author-place">From London, UK</p></div></div>
</div>
<a class="abs btn btn-cases">Read Case Studies</a>

<footer class="abs footer">
  <p class="footer-heading">Company</p>
  <ul class="footer-links">
    <li>About Us</li><li>Contact Us</li><li>Newsroom</li><li>Investor Relations</li><li>Annual Returns</li><li>Careers</li><li>Legal</li><li>Blog</li><li>Trust Center</li>
  </ul>
</footer>
<div class="abs bottom-bar">©2019. Panelcraft. All Rights Reserved.</div>

</body>
</html>
```